Awesome photographers card for an awesome new business

Double sided business card Black background and silver logo in middle on one side. Details on otherside. please keep it simple

Photographer

Gavin Tolley
0482615073
GavinTolleyPhotography82@lumenpost.com
www.GavinTolleyPhotography.com.au
Instagram _Gavin_tolley

Requirements
Must have
• My logo in Silver
• please use instagram logo instead of "Instagram"

```html
<!DOCTYPE html>
<html lang="en">
<head>
<meta charset="utf-8">
<title>Gavin Tolley Photography – Business Card</title>
<link rel="stylesheet" href="https://fonts.googleapis.com/css2?family=Allura&family=Poppins:ital,wght@0,300;1,300&display=swap">
<style>
  :root {
    --page: #ffffff;
    --card: #050706;
    --silver: #d2d2d2;
    --silver-soft: #c4c4c4;
  }
  html, body {
    margin: 0;
    padding: 0;
    width: 879px;
    height: 1200px;
    overflow: hidden;
    background: var(--page);
  }
  .sheet {
    position: relative;
    width: 879px;
    height: 1200px;
  }
  .card {
    position: absolute;
    left: 0;
    width: 878px;
    background: var(--card);
  }
  .card--front { top: 0; height: 577px; }
  .card--back { top: 621px; height: 579px; }
  .card svg {
    display: block;
    width: 100%;
    height: 100%;
  }

  .brand__mark { fill: var(--silver); }
  .brand__name {
    font-family: "Poppins", sans-serif;
    font-weight: 300;
    font-size: 64px;
    fill: var(--silver);
  }

  .back__name {
    font-family: "Allura", cursive;
    font-size: 104px;
    fill: var(--silver);
  }
  .back__role,
  .contact__line {
    font-family: "Poppins", sans-serif;
    font-style: italic;
    font-weight: 300;
    font-size: 30px;
    fill: var(--silver-soft);
  }
</style>
</head>
<body>
<main class="sheet">
  <section class="card card--front" aria-label="Card front">
    <svg viewBox="0 0 878 577" xmlns="http://www.w3.org/2000/svg">
      <circle class="brand__mark" cx="250" cy="286" r="16"/>
      <text class="brand__name" x="284" y="309" textLength="360" lengthAdjust="spacingAndGlyphs">Gavin Tolley</text>
    </svg>
  </section>

  <section class="card card--back" aria-label="Card back">
    <svg viewBox="0 0 878 579" xmlns="http://www.w3.org/2000/svg">
      <text class="back__name" x="34" y="96" textLength="624" lengthAdjust="spacingAndGlyphs">Gavin Tolley</text>
      <text class="back__role" x="448" y="138" textLength="229" lengthAdjust="spacingAndGlyphs">Photographer</text>
      <g class="contact">
        <text class="contact__line" x="34" y="371" textLength="197" lengthAdjust="spacingAndGlyphs">0482615073</text>
        <text class="contact__line" x="34" y="411" textLength="632" lengthAdjust="spacingAndGlyphs">GavinTolleyPhotography82@lumenpost.com</text>
        <text class="contact__line" x="34" y="449" textLength="617" lengthAdjust="spacingAndGlyphs">www.GavinTolleyPhotography.com.au</text>
        <text class="contact__line" x="34" y="488" textLength="410" lengthAdjust="spacingAndGlyphs">Instagram  _Gavin_tolley</text>
      </g>
    </svg>
  </section>
</main>
</body>
</html>
```